New web design needed for our company

We need our website designing, it needs to be professional and look creative,
We are a plumbing and heating company called Kestrel Bay's (www.kestrelbays.co.uk)
I like this site design also some of the following maybe:
https://www.marnockheating.com/
http://www.tavelpower.co.uk

Please let me know when you want our logo files as it wont let me upload them

The design will require coding once the design is complete, i havent paid for this yet as i want to be sure the design is good before i commit.

The template needs to look professional and look like one of the leading companies.
The site will consist of all the features this site has https://www.marnockheating.com/

I like a modern design with the latest technology.

Must have a customer login page and a my account area

Target Market(s)

Everyone

Industry/Entity Type

Plumbing

Coding

Coded - Design and coding required

Number of Pages Required

5+ page

Font styles to use
Other font styles liked:
• whatever suites

Requirements
Must have
• The design will require coding once the design is complete, i havent paid for this yet as i want to be sure the design is good before i commit.
• The template needs to look professional and look like one of the leading companies.
• The site will consist of all the features this site has https://www.marnockheating.com/
• I like a modern design with the latest technology.
• Must have a customer login page and a my account area
Nice to have
• inspirational and different
Should not have
• plain boring designs like most plumbing websites, needs to be inspiring and attract people from first sight.

```html
<!DOCTYPE html>
<html lang="en">
<head>
<meta charset="utf-8">
<title>Kestrel Bay's – Plumbing &amp; Heating</title>
<link href="https://fonts.googleapis.com/css2?family=Montserrat:wght@400;500;600;700&family=Open+Sans:wght@400;600&display=swap" rel="stylesheet">
<style>
:root{
  --orange:#f4623a;
  --navy:#1d2c6b;
  --ink:#333b4a;
  --muted:#666;
  --line:#dcdcdc;
  --panel:#f3f3f3;
  --footer:#333333;
  --white:#fff;
}
*{box-sizing:border-box;margin:0;padding:0}
html,body{width:1200px;height:3010px;overflow:hidden}
body{position:relative;background:var(--white);font-family:"Open Sans",Arial,sans-serif;color:var(--ink)}
.abs{position:absolute}

/* top bar */
.topbar{left:110px;top:0;width:980px;height:32px;background:var(--orange);clip-path:polygon(0 0,100% 0,97% 100%,3% 100%)}
.topbar .social{position:absolute;left:46px;top:9px;display:flex;gap:10px}
.topbar .social span{width:12px;height:12px;border-radius:50%;background:var(--white);opacity:.9}
.topbar .util{position:absolute;top:0;line-height:30px;font-size:11px;color:var(--white);font-family:Montserrat,Arial,sans-serif;display:flex;align-items:center;gap:6px}
.quick-find{left:760px;top:0;width:290px;height:32px;background:var(--navy);color:var(--white);font:500 11px/32px Montserrat,Arial,sans-serif;padding-left:14px}
.quick-find svg{position:absolute;right:16px;top:10px}

/* header */
.brand{left:156px;top:44px;font:700 32px/1 Montserrat,Arial,sans-serif;color:var(--navy);letter-spacing:-.5px}
.main-nav{left:382px;top:62px;display:flex;font:600 12px/1 Montserrat,Arial,sans-serif;color:var(--navy)}
.main-nav a{color:inherit;text-decoration:none;padding:0 9px;border-right:1px solid var(--navy)}
.main-nav a:first-child{padding-left:0}
.main-nav a:last-child{border-right:0}
.main-nav a.active{color:var(--orange);position:relative}
.main-nav a.active::after{content:"";position:absolute;left:0;right:9px;bottom:-8px;height:2px;background:var(--orange)}

/* hero */
.hero{left:156px;top:104px;width:658px;height:318px;background:linear-gradient(135deg,#3d5fa8,#2c4a92 55%,#4b6fb6)}
.hero-title{left:0;top:94px;width:658px;text-align:center;color:var(--white);font:600 25px/32px Montserrat,Arial,sans-serif}
.btn{display:inline-block;background:var(--orange);color:var(--white);font:500 12px/28px Montserrat,Arial,sans-serif;text-align:center}
.hero .btn{position:absolute;left:264px;top:184px;width:126px}
.side-card{left:836px;width:206px;color:var(--white)}
.side-card .label{position:absolute;left:0;right:0;text-align:center;font:700 16px/20px Montserrat,Arial,sans-serif}
.side-card .strip{position:absolute;left:0;right:0;bottom:0;height:26px;font:500 12px/26px Montserrat,Arial,sans-serif;text-align:center}
.card-boiler{top:104px;height:152px;background:linear-gradient(160deg,#8ea0b4,#5a6d86)}
.card-boiler .strip{background:var(--orange)}
.card-move{top:274px;height:148px;background:linear-gradient(160deg,#6b6a5d,#3e4038)}
.card-move .strip{background:var(--navy)}

/* section titles */
.sec-title{left:0;width:1200px;text-align:center;font:700 17px/1 Montserrat,Arial,sans-serif;color:var(--navy);letter-spacing:.5px}
.sec-title em{font-style:normal;color:var(--orange)}
.sec-dot{width:10px;height:10px;border-radius:50%;background:var(--orange);left:595px}

/* quick tasks */
.tasks{left:156px;top:548px;display:flex;gap:23.6px}
.task{width:128px;height:120px;border:1px solid var(--line);background:var(--white);text-align:center;color:var(--navy);font:600 11px/15px Montserrat,Arial,sans-serif;padding-top:18px}
.task svg{display:block;margin:0 auto 8px}
.task .rule{width:22px;height:2px;background:var(--orange);margin:0 auto 6px}
.task.active{background:var(--orange);color:var(--white);border-color:var(--orange)}
.task.active .rule{background:var(--white)}

/* services */
.panel{left:0;width:1200px;background:var(--panel)}
.service{width:280px;text-align:center}
.service svg{display:block;margin:0 auto}
.service h3{font:700 14px/1 Montserrat,Arial,sans-serif;color:var(--navy);margin-top:14px}
.service .rule{width:26px;height:2px;background:var(--orange);margin:9px auto 12px}
.service p{font-size:11px;line-height:16px;color:var(--muted)}
.service .more{display:block;margin:24px auto 0;color:var(--orange);font-size:16px;line-height:1}
.service .more.on{width:28px;height:28px;border-radius:50%;background:var(--orange);color:var(--white);line-height:28px;font-size:14px;margin-top:12px}

/* form */
.field{border:1px solid var(--line);height:32px;font-size:11px;color:#999;padding:0 10px;line-height:30px;background:var(--white)}

/* gallery */
.tile-plumber{background:linear-gradient(135deg,#f47a5c,#e7573a)}
.tile-plumber .link{position:absolute;left:196px;top:74px;width:38px;height:38px;border-radius:50%;background:var(--white)}
.tile-sink{background:linear-gradient(150deg,#e8ecef,#3d5ea6 70%,#c8d2dc)}
.tile-bath{background:linear-gradient(160deg,#c8c0b6,#8c8174)}
.tile-vanity{background:linear-gradient(160deg,#4a5a44,#2d2d2b)}
.tile-tap{background:linear-gradient(160deg,#f0f1f0,#b9bdbf)}
.tile-tub{background:linear-gradient(160deg,#a8a49d,#6f6c67)}

/* testimonial */
.avatar{left:306px;top:2450px;width:90px;height:96px;background:linear-gradient(160deg,#c7a88e,#7a8a9a)}
.name-tag{left:396px;top:2464px;width:136px;height:28px;background:var(--orange);color:var(--white);font:500 12px/28px Montserrat,Arial,sans-serif;padding-left:12px;clip-path:polygon(0 0,100% 0,92% 100%,0 100%)}
.quote{left:456px;top:2512px;width:440px;font-size:13px;line-height:20px;font-style:italic;color:var(--ink)}
.quote-mark{left:410px;top:2502px;font:700 34px/1 Georgia,serif;color:#5aa7d6}
.dots{left:580px;top:2580px;display:flex;gap:8px}
.dots span{width:8px;height:8px;border-radius:50%;background:var(--navy)}
.dots span.on{background:var(--orange)}

/* footer */
.footer{left:0;top:2636px;width:1200px;height:324px;background:var(--footer);color:#ddd}
.footer h4{position:absolute;top:52px;font:700 12px/1 Montserrat,Arial,sans-serif;color:var(--white);letter-spacing:.5px}
.footer .brand-foot{position:absolute;left:156px;top:46px;font:700 28px/1 Montserrat,Arial,sans-serif;color:var(--orange)}
.footer .about{position:absolute;left:156px;top:112px;width:180px;font-size:12px;line-height:17px;color:#ccc}
.footer .btn{position:absolute;left:156px;top:204px;width:96px}
.footer .fsocial{position:absolute;left:156px;top:256px;display:flex;gap:10px}
.footer .fsocial span{width:24px;height:24px;border-radius:50%;background:#888}
.footer .fsocial span.on{background:var(--orange)}
.links{position:absolute;left:382px;top:114px;list-style:none;font-size:12px;line-height:24px;color:#ccc}
.links li::before{content:"» ";color:#ccc}
.footer .field{position:absolute;left:586px;width:204px;height:30px;background:transparent;border-color:#777;color:#ccc;line-height:28px}
.footer .signup{position:absolute;left:586px;top:206px;width:96px}
.contact{position:absolute;left:838px;color:#ccc;font-size:12px;line-height:17px}
.phone{position:absolute;left:838px;top:240px;font:400 20px/1 Montserrat,Arial,sans-serif;color:#ddd}
.email{position:absolute;left:838px;top:264px;font-size:12px;color:var(--orange);text-decoration:underline}
.bottom-bar{left:0;top:2960px;width:1200px;height:50px;background:var(--orange);color:var(--white);font:500 11px/40px Montserrat,Arial,sans-serif;padding-left:156px}
.to-top{position:absolute;right:154px;top:10px;width:20px;height:20px;border-radius:50%;background:var(--white)}
</style>
</head>
<body>

<!-- top bar -->
<div class="abs topbar">
  <div class="social"><span></span><span></span><span></span></div>
  <div class="util" style="left:352px">
    <svg width="11" height="11" viewBox="0 0 12 12"><path d="M1 6h7M5 3l3 3-3 3M8 1h3v10H8" fill="none" stroke="#fff" stroke-width="1.4"/></svg>
    Sign In &amp; Register
  </div>
  <div class="util" style="left:470px">
    <svg width="11" height="11" viewBox="0 0 12 12"><path d="M2 8V6a4 4 0 018 0v2" fill="none" stroke="#fff" stroke-width="1.4"/><rect x="1" y="7" width="2.5" height="3.5" fill="#fff"/><rect x="8.5" y="7" width="2.5" height="3.5" fill="#fff"/></svg>
    Support: +123-456-7890
  </div>
</div>
<div class="abs quick-find">Quick Find Service
  <svg width="12" height="12" viewBox="0 0 12 12"><circle cx="5" cy="5" r="3.8" fill="none" stroke="#fff" stroke-width="1.6"/><path d="M8 8l3 3" stroke="#fff" stroke-width="1.8"/></svg>
</div>

<!-- header -->
<div class="abs brand">Kestrel Bay's</div>
<nav class="abs main-nav">
  <a class="active">Home</a><a>My Account</a><a>Service</a><a>Emergencies</a><a>Business Customers</a><a>Bay Care</a><a>Help and Support</a>
</nav>

<!-- hero -->
<div class="abs hero" role="img" aria-label="Blue-toned modern bathroom with freestanding bath and basin">
  <div class="abs hero-title">We Are Services To Fix Your<br>Plumbing Issuse</div>
  <span class="btn">Appointment</span>
</div>
<div class="abs side-card card-boiler" role="img" aria-label="Engineer servicing a boiler">
  <div class="label" style="top:42px">Boiler repairs &amp;<br>maintenance</div>
  <div class="strip">Get Repair</div>
</div>
<div class="abs side-card card-move" role="img" aria-label="Living room of a new home">
  <div class="label" style="top:48px">Moving Home?</div>
  <div class="strip">Move Home</div>
</div>

<!-- what are you looking to do -->
<div class="abs sec-dot" style="top:472px"></div>
<div class="abs sec-title" style="top:502px">WHAT ARE YOU <em>LOOKING TO DO?</em></div>
<div class="abs tasks">
  <div class="task">
    <svg width="30" height="26" viewBox="0 0 30 26"><rect x="2" y="4" width="26" height="18" rx="2" fill="none" stroke="#1d2c6b" stroke-width="2"/><path d="M2 10h26" stroke="#1d2c6b" stroke-width="3"/><path d="M6 17h8" stroke="#f4623a" stroke-width="2"/></svg>
    <div class="rule"></div>Pay Your<br>Bil
  </div>
  <div class="task">
    <svg width="30" height="26" viewBox="0 0 30 26"><rect x="3" y="4" width="24" height="20" fill="none" stroke="#1d2c6b" stroke-width="2"/><path d="M3 9h24M9 1v6M21 1v6M8 13h3M14 13h3M20 13h3M8 18h3M14 18h3" stroke="#1d2c6b" stroke-width="2"/></svg>
    <div class="rule"></div>Book An<br>Engineer
  </div>
  <div class="task active">
    <svg width="30" height="26" viewBox="0 0 30 26"><rect x="6" y="1" width="18" height="24" fill="none" stroke="#fff" stroke-width="2"/><path d="M10 7h10M10 11h10" stroke="#fff" stroke-width="2"/><circle cx="15" cy="18" r="3" fill="none" stroke="#fff" stroke-width="2"/></svg>
    <div class="rule"></div>I Need A landlord<br>Certificate
  </div>
  <div class="task">
    <svg width="30" height="26" viewBox="0 0 30 26"><rect x="3" y="2" width="24" height="16" fill="none" stroke="#1d2c6b" stroke-width="2"/><path d="M11 24h8M15 18v6" stroke="#1d2c6b" stroke-width="2"/><circle cx="15" cy="9" r="3" fill="#f4623a"/></svg>
    <div class="rule"></div>Manage Your<br>Account
  </div>
  <div class="task">
    <svg width="30" height="26" viewBox="0 0 30 26"><path d="M5 3l20 20M25 3L5 23" stroke="#1d2c6b" stroke-width="2.4"/><circle cx="5" cy="3" r="2.5" fill="#f4623a"/><circle cx="25" cy="3" r="2.5" fill="#f4623a"/></svg>
    <div class="rule"></div>Need A Boiler<br>Service
  </div>
  <div class="task">
    <svg width="30" height="26" viewBox="0 0 30 26"><rect x="5" y="2" width="20" height="20" rx="3" fill="#1d2c6b"/></svg>
    <div class="rule"></div>Set Up A Direct<br>Debit
  </div>
</div>

<!-- services -->
<div class="abs panel" style="top:716px;height:588px"></div>
<div class="abs sec-dot" style="top:752px"></div>
<div class="abs sec-title" style="top:780px">SERVICES WE <em>ARE OFFERING</em></div>

<div class="abs service" style="left:156px;top:842px">
  <svg width="50" height="50" viewBox="0 0 50 50"><path d="M4 8h22v10h8v6" fill="none" stroke="#1d2c6b" stroke-width="3"/><path d="M4 14h16v10h8" fill="none" stroke="#1d2c6b" stroke-width="3"/><path d="M31 32c-3 5-3 8 0 9 3-1 3-4 0-9z" fill="none" stroke="#1d2c6b" stroke-width="2.2"/></svg>
  <h3>PlumbBay's</h3><div class="rule"></div>
  <p>But I must explain to you how all this<br>taken idea of denouncing...</p><span class="more">→</span>
</div>
<div class="abs service" style="left:458px;top:842px">
  <svg width="50" height="50" viewBox="0 0 50 50"><circle cx="20" cy="18" r="10" fill="none" stroke="#1d2c6b" stroke-width="3"/><path d="M16 22l8-8M6 34h38M30 28v12M8 28v12" stroke="#1d2c6b" stroke-width="3" fill="none"/></svg>
  <h3>GasBay's</h3><div class="rule"></div>
  <p>But I must explain to you how all this<br>taken idea of denouncing...</p><span class="more on">→</span>
</div>
<div class="abs service" style="left:760px;top:842px">
  <svg width="50" height="50" viewBox="0 0 50 50"><path d="M4 24h42M4 34h42M4 24v10M46 24v10" stroke="#1d2c6b" stroke-width="3" fill="none"/><rect x="18" y="18" width="14" height="22" fill="none" stroke="#1d2c6b" stroke-width="3"/><path d="M25 18V8M19 6h12" stroke="#1d2c6b" stroke-width="3"/></svg>
  <h3>OilBay's</h3><div class="rule"></div>
  <p>But I must explain to you how all this<br>taken idea of denouncing...</p><span class="more">→</span>
</div>

<div class="abs service" style="left:156px;top:1082px">
  <svg width="50" height="50" viewBox="0 0 50 50"><path d="M4 8h22v10h8v6" fill="none" stroke="#1d2c6b" stroke-width="3"/><path d="M4 14h16v10h8" fill="none" stroke="#1d2c6b" stroke-width="3"/><path d="M31 32c-3 5-3 8 0 9 3-1 3-4 0-9z" fill="none" stroke="#1d2c6b" stroke-width="2.2"/></svg>
  <h3>DrainBay's</h3><div class="rule"></div>
  <p>But I must explain to you how all this<br>taken idea of denouncing...</p><span class="more">→</span>
</div>
<div class="abs service" style="left:458px;top:1082px">
  <svg width="50" height="50" viewBox="0 0 50 50"><circle cx="20" cy="18" r="10" fill="none" stroke="#1d2c6b" stroke-width="3"/><path d="M16 22l8-8M6 34h38M30 28v12M8 28v12" stroke="#1d2c6b" stroke-width="3" fill="none"/></svg>
  <h3>PowerBay's</h3><div class="rule"></div>
  <p>But I must explain to you how all this<br>taken idea of denouncing...</p><span class="more">→</span>
</div>
<div class="abs service" style="left:760px;top:1078px">
  <svg width="50" height="50" viewBox="0 0 50 50"><path d="M4 24h42M4 34h42M4 24v10M46 24v10" stroke="#1d2c6b" stroke-width="3" fill="none"/><rect x="18" y="18" width="14" height="22" fill="none" stroke="#1d2c6b" stroke-width="3"/><path d="M25 18V8M19 6h12" stroke="#1d2c6b" stroke-width="3"/></svg>
  <h3>PowerBay's</h3><div class="rule"></div>
  <p>But I must explain to you how all this<br>taken idea of denouncing...</p><span class="more">→</span>
</div>

<!-- question form -->
<div class="abs sec-dot" style="top:1358px"></div>
<div class="abs sec-title" style="top:1386px">GOT A <em>QUESTION?</em></div>
<div class="abs field" style="left:156px;top:1434px;width:430px">Name :</div>
<div class="abs field" style="left:610px;top:1434px;width:432px">Email :</div>
<div class="abs field" style="left:156px;top:1482px;width:430px">Phone :</div>
<div class="abs field" style="left:610px;top:1482px;width:432px">Address :</div>
<div class="abs field" style="left:156px;top:1532px;width:886px;height:72px">Service You Need ?</div>
<span class="abs btn" style="left:536px;top:1638px;width:124px">Get A Request</span>

<!-- gallery -->
<div class="abs panel" style="top:1714px;height:610px"></div>
<div class="abs sec-dot" style="top:1756px"></div>
<div class="abs sec-title" style="top:1778px">OUR PROJECT <em>GALLERY</em></div>
<div class="abs tile-plumber" style="left:156px;top:1832px;width:430px;height:186px" role="img" aria-label="Plumber fitting pipework under a sink, orange overlay"><span class="link"></span></div>
<div class="abs tile-sink" style="left:610px;top:1832px;width:204px;height:186px" role="img" aria-label="Plumber in blue overalls repairing a basin"></div>
<div class="abs tile-bath" style="left:836px;top:1832px;width:206px;height:186px" role="img" aria-label="Freestanding bath in a tiled bathroom"></div>
<div class="abs tile-vanity" style="left:156px;top:2042px;width:204px;height:186px" role="img" aria-label="Vanity unit with basin against a green wall"></div>
<div class="abs tile-tap" style="left:382px;top:2042px;width:204px;height:186px" role="img" aria-label="Chrome kitchen tap beside a plant"></div>
<div class="abs tile-tub" style="left:610px;top:2042px;width:432px;height:186px" role="img" aria-label="Built-in bathtub filled with water"></div>
<span class="abs btn" style="left:536px;top:2262px;width:124px">View All</span>

<!-- testimonial -->
<div class="abs sec-dot" style="top:2372px"></div>
<div class="abs sec-title" style="top:2404px">WHAT OUR <em>CLIENT SAYS</em></div>
<div class="abs avatar" role="img" aria-label="Portrait of client"></div>
<div class="abs name-tag">Dolore Magna</div>
<div class="abs quote-mark">“</div>
<p class="abs quote">Lorem ipsum dolor sit amet, consectetur adipiscing elit, sed do eiusmod tempor incididunt ut labore et.</p>
<div class="abs dots"><span></span><span class="on"></span><span></span></div>

<!-- footer -->
<footer class="abs footer">
  <div class="brand-foot">Kestrel Bay's</div>
  <p class="about">Sed ut perspiciatis unde omnis iste natus error sit voluptatem accusantium doloremque laudantium, totam...</p>
  <span class="btn">Read More</span>
  <div class="fsocial"><span></span><span class="on"></span><span></span></div>

  <h4 style="left:382px">SITE LINKS</h4>
  <ul class="links">
    <li>Home</li><li>My Account</li><li>Service</li><li>Emergencies</li><li>Business Customers</li><li>Bay Care</li><li>Help and Support</li>
  </ul>

  <h4 style="left:586px">NEWSLETTER</h4>
  <div class="field" style="top:110px">Name :</div>
  <div class="field" style="top:158px">Email :</div>
  <span class="btn signup">Sign Up</span>

  <h4 style="left:838px">CONTACT US</h4>
  <svg class="abs" style="left:838px;top:112px" width="20" height="26" viewBox="0 0 20 26"><path d="M10 24S2 14 2 9a8 8 0 0116 0c0 5-8 15-8 15z" fill="none" stroke="#f4623a" stroke-width="2"/><circle cx="10" cy="9" r="3" fill="none" stroke="#f4623a" stroke-width="2"/></svg>
  <p class="contact" style="top:154px">At vero eos et accusamus et<br>iusto odio 12345</p>
  <svg class="abs" style="left:838px;top:208px" width="22" height="22" viewBox="0 0 22 22"><path d="M5 2l4 4-2 3c1 3 3 5 6 6l3-2 4 4-3 4C9 21 1 13 1 5z" fill="none" stroke="#f4623a" stroke-width="2"/></svg>
  <div class="phone">123-456-7890</div>
  <div class="email">info@kestrelbays.com</div>
</footer>
<div class="abs bottom-bar">© 2016 Kestrel Bay's UK Limited,&nbsp;&nbsp;&nbsp;All rights reserved.
  <span class="to-top"><svg width="20" height="20" viewBox="0 0 20 20"><path d="M6 11l4-4 4 4" fill="none" stroke="#f4623a" stroke-width="2"/></svg></span>
</div>

</body>
</html>
```